DL, Tri Fold Flyer - Keen On Labs

We need DL Tri Fold Brochure designed to print and distribute to primary schools in Australia advertising our exciting and educational science workshops.

Fun, exciting yet with a professional/educational edge. Similar to the feel of our website science shop www.keenonlabs.com.au and/or incursion page keenonlabsvisits.com.au

Design should be fresh, clean and simple, eye-catching with a sense of quality.

There needs to be visual interest with graphic elements and pictures to break up the text. To be print ready with bleed and cut lines indicated for printer. Roll fold, 2 -sided, and full colour.

The font cover image spills on to the back cover and needs to relate to the Quest Fortnight theme for 2020: Innovations for the future of our oceans. Perhaps eye-catching offshore ocean turbines (with or without ocean life underneath)? Example images attached, can use an image from Pixwharf library.

This is a link to brochures printed in the past to give you an idea of design and layout.

Can use images of our presenters/kids on facebook page to break up text - www.facebook.com/keenonlabs

Please see the attached file MadAboutScienceBrochureDesignBrief2020 for complete text and layout requirements - this file is coming soon.

Target Market(s)

Primary School Teachers

Colors

Designer to choose colors to be used in the design.

Requirements
Must have
• 1. Eye-catching front image picture, spilling on to back cover
• 2. Quality feel
• 3. Images to break up text

```html
<!DOCTYPE html>
<html lang="en">
<head>
<meta charset="utf-8">
<title>Keen On Labs – DL Tri Fold Brochure</title>
<link href="https://fonts.googleapis.com/css2?family=Oswald:wght@500;700&family=Montserrat:wght@600;800&family=Open+Sans:wght@400;600;700&display=swap" rel="stylesheet">
<style>
:root{
  --navy:#0b1d4a;
  --deep:#0f2f73;
  --blue:#1b5fb8;
  --sky:#2f94dc;
  --yellow:#f6c415;
  --red:#e2262f;
  --green:#3aa84a;
  --purple:#6b3fa0;
  --orange:#f08a1c;
  --ink:#1c2333;
  --paper:#ffffff;
  --bg:#eef1f5;
}
*{box-sizing:border-box;margin:0;padding:0}
html,body{width:1200px;height:2632px;overflow:hidden}
body{background:var(--bg);font-family:"Open Sans",Arial,sans-serif;color:var(--ink);position:relative}
.label{position:absolute;left:40px;font:700 22px "Montserrat",Arial,sans-serif;letter-spacing:2px;color:var(--navy)}
.spread{position:absolute;left:40px;width:1120px;background:var(--paper);box-shadow:0 6px 20px rgba(0,0,0,.18);display:flex;overflow:hidden}
.outside{top:90px;height:790px}
.inside{top:990px;height:1610px;flex-direction:column}
.panel{width:373.33px;height:100%;position:relative;overflow:hidden}
.panel + .panel{border-left:1px dashed rgba(0,0,0,.12)}

.brand{display:flex;align-items:center;gap:10px;justify-content:center}
.brand .dot{width:26px;height:26px;border-radius:50%;background:var(--yellow)}
.brand .name{font:800 30px "Montserrat",Arial,sans-serif;color:#fff}
.brand-sub{font:700 15px "Montserrat",Arial,sans-serif;color:#fff;letter-spacing:3px;text-align:center;margin-top:4px}

.info{padding:26px 24px}
.info h3{font:700 22px "Oswald",Arial,sans-serif;color:var(--blue);margin-bottom:10px;letter-spacing:.5px}
.info p{font-size:11.5px;line-height:1.55;margin-bottom:10px}
.price{background:var(--blue);color:#fff;font:700 12px "Open Sans",Arial,sans-serif;padding:6px 10px;margin-bottom:5px;border-radius:3px}
.price.alt{background:var(--sky)}
.kinder{background:var(--navy);color:#fff;font:700 17px "Oswald",Arial,sans-serif;padding:8px 12px;margin:14px 0 10px;border-radius:3px;letter-spacing:.5px}
.photo{background:linear-gradient(135deg,#c9a37e,#6f8fb8 60%,#2d4d80)}
.p1-photo{position:absolute;left:0;right:0;bottom:0;height:190px}

.p2{background:var(--deep)}
.why{background:var(--yellow);margin:22px 22px 0;padding:14px 18px;border-radius:6px}
.why h3{font:700 24px "Oswald",Arial,sans-serif;color:var(--navy);margin-bottom:8px;text-align:center}
.why li{list-style:none;display:flex;gap:8px;align-items:center;font:700 12.5px "Open Sans",Arial,sans-serif;color:var(--navy);margin:6px 0}
.why svg{flex:none}
.p2 .brand{margin-top:30px}
.p2-sea{position:absolute;left:0;right:0;bottom:0;height:430px;background:linear-gradient(180deg,#1c6fb3,#0d3d7a 55%,#071a3d)}
.book{position:absolute;left:26px;top:40px;width:120px;height:120px;border-radius:50%;background:var(--yellow);display:flex;align-items:center;justify-content:center;text-align:center;font:700 15px/1.15 "Oswald",Arial,sans-serif;color:var(--navy)}
.contact{position:absolute;left:0;right:0;bottom:26px;text-align:center;color:#fff;font-size:11.5px;line-height:1.7}
.contact strong{font-family:"Montserrat",Arial,sans-serif;font-size:14px}

.cover{background:linear-gradient(180deg,#0a2a66 0%,#1460ad 38%,#0f4d8f 62%,#061634 100%)}
.cover .brand{margin-top:60px}
.cover-title{text-align:center;color:#fff;font:700 34px/1.05 "Oswald",Arial,sans-serif;margin-top:34px;letter-spacing:1px;position:relative}
.cover-title span{display:block;font-size:48px;color:var(--yellow)}
.cover-photo{position:absolute;left:0;right:0;top:300px;height:250px;background:radial-gradient(ellipse at 50% 40%,#3fa1d8,#0d4d8f 70%,transparent)}
.cover-tag{position:absolute;left:0;right:0;bottom:60px;text-align:center;color:#fff}
.cover-tag .year{font:700 20px "Oswald",Arial,sans-serif;color:var(--yellow)}
.cover-tag .main{font:700 30px/1.05 "Oswald",Arial,sans-serif}
.cover-tag .state{display:inline-block;margin-top:10px;background:var(--red);padding:4px 14px;font:700 15px "Montserrat",Arial,sans-serif;border-radius:3px}
.cover-foot{position:absolute;left:0;right:0;bottom:16px;text-align:center;color:#fff;font:600 12px "Open Sans",Arial,sans-serif}

.inside-cols{display:flex;flex:1;min-height:0}
.col{width:373.33px;padding:18px 18px 16px;display:flex;flex-direction:column;justify-content:space-between;overflow:hidden}
.col + .col{border-left:1px dashed rgba(0,0,0,.12)}
.head-band{background:linear-gradient(135deg,var(--navy),var(--blue));margin:-18px -18px 0;padding:22px 18px}
.head-band .brand .name{font-size:26px}
.head-band p{color:#dfe9fb;font-size:11.5px;text-align:center;margin-top:8px}
.sect{color:#fff;font:700 16px "Oswald",Arial,sans-serif;letter-spacing:.8px;padding:6px 10px;border-radius:3px;text-align:center}
.chem{background:var(--red)}.phys{background:var(--blue)}.bio{background:var(--green)}.earth{background:var(--orange)}.stem{background:var(--purple)}
.item h4{font:700 13px "Montserrat",Arial,sans-serif;color:var(--navy);margin-bottom:2px}
.item h4 span{color:var(--red);font-weight:600;font-size:11.5px}
.item p{font-size:12px;line-height:1.5}
.snap{flex:0 0 130px;border-radius:4px}
.foot{height:54px;flex:none;background:var(--navy);color:#fff;display:flex;justify-content:space-around;align-items:center;font:600 14px "Montserrat",Arial,sans-serif}
.foot span{display:flex;align-items:center;gap:8px}
</style>
</head>
<body>

<div class="label" style="top:44px">BROCHURE OUTSIDE</div>
<section class="spread outside">
  <div class="panel">
    <div class="info">
      <h3>DURATION &amp; COST</h3>
      <p>Our interactive science sessions run for one hour. We can fit two to four classes into a day, tailored to your school timetable and class sizes.</p>
      <p>Each session is priced per student with a minimum booking. Bigger bookings on the same day earn a discount.</p>
      <div class="price">$260 for a 60 minute workshop (up to 30)</div>
      <div class="price alt">$290 for a 60 minute workshop (up to 40)</div>
      <p>Additional students are charged at a flat rate per head. All materials, safety gear and clean up are included in the price.</p>
      <div class="kinder">KINDERGARTEN SESSIONS</div>
      <p>Our early learners program is shorter and hands on, built for little hands and big curious minds. Sessions last 45 minutes.</p>
      <div class="price">$240 for a single 45 minute kinder session</div>
      <div class="price alt">$430 for two back to back kinder sessions</div>
    </div>
    <div class="photo p1-photo" role="img" aria-label="Photo of a presenter running a science demonstration with primary school children"></div>
  </div>

  <div class="panel p2">
    <div class="why">
      <h3>Why Choose Us?</h3>
      <ul>
        <li><svg width="16" height="16" viewBox="0 0 16 16"><circle cx="8" cy="8" r="8" fill="#0b1d4a"/><path d="M4 8l3 3 5-6" stroke="#f6c415" stroke-width="2" fill="none"/></svg>Seriously fun and engaging</li>
        <li><svg width="16" height="16" viewBox="0 0 16 16"><circle cx="8" cy="8" r="8" fill="#0b1d4a"/><path d="M4 8l3 3 5-6" stroke="#f6c415" stroke-width="2" fill="none"/></svg>Lead by science teaching specialists</li>
        <li><svg width="16" height="16" viewBox="0 0 16 16"><circle cx="8" cy="8" r="8" fill="#0b1d4a"/><path d="M4 8l3 3 5-6" stroke="#f6c415" stroke-width="2" fill="none"/></svg>Packed full of hands-on experimenting</li>
        <li><svg width="16" height="16" viewBox="0 0 16 16"><circle cx="8" cy="8" r="8" fill="#0b1d4a"/><path d="M4 8l3 3 5-6" stroke="#f6c415" stroke-width="2" fill="none"/></svg>Aligned with curriculum outcomes</li>
      </ul>
    </div>
    <div class="brand"><span class="dot"></span><span class="name">Keen On Labs</span></div>
    <div class="brand-sub">IN SCHOOLS</div>
    <div class="p2-sea" role="img" aria-label="Underwater ocean photo with a sea turtle swimming">
      <div class="book">BOOK A WORKSHOP &amp; MORE INFO</div>
      <div class="contact">
        PO Box 100, Sampleton NSW 2000<br>
        <strong>1300 555 014</strong><br>
        hello@keenonlabs.com.au<br>
        keenonlabsvisits.com.au
      </div>
    </div>
  </div>

  <div class="panel cover">
    <div class="brand"><span class="dot"></span><span class="name">Keen On Labs</span></div>
    <div class="brand-sub">IN SCHOOLS</div>
    <div class="cover-photo" role="img" aria-label="Ocean scene with offshore turbines above and a turtle below the surface"></div>
    <div class="cover-title">THE POWER OF<span>THE DEEP BLUE</span></div>
    <div class="cover-tag">
      <div class="year">2020 PRIMARY SCHOOL</div>
      <div class="main">SCIENCE WORKSHOPS<br>&amp; INCURSIONS</div>
      <div class="state">Now in NSW and QLD</div>
    </div>
    <div class="cover-foot">Call us 1300 555 014 · keenonlabsvisits.com.au</div>
  </div>
</section>

<div class="label" style="top:944px">BROCHURE INSIDE</div>
<section class="spread inside">
  <div class="inside-cols">
    <div class="col">
      <div class="head-band">
        <div class="brand"><span class="dot"></span><span class="name">Keen On Labs</span></div>
        <div class="brand-sub">IN SCHOOLS</div>
        <p>Choose any workshop below to suit your class and curriculum unit.</p>
      </div>
      <div class="sect chem">CHEMICAL SCIENCES</div>
      <div class="item"><h4>Kitchen Chemistry <span>Foundation to Level 2</span></h4><p>Students mix, measure and observe everyday kitchen materials changing in surprising and colourful ways.</p></div>
      <div class="item"><h4>The Matter of Mixing <span>Level 3 &amp; 4</span></h4><p>Explore solids, liquids and gases while testing how adding or removing heat changes each state.</p></div>
      <div class="item"><h4>Fizz, Pop &amp; Bang <span>Level 5 &amp; 6</span></h4><p>Safe reactions show students how new substances form and how energy is released as heat and gas.</p></div>
      <div class="item"><h4>Polymer Play <span>Level 3 &amp; 4</span></h4><p>Make stretchy slime and bouncy balls, then learn why long chain molecules behave so strangely.</p></div>
      <div class="item"><h4>Colour Detectives <span>Foundation to Level 2</span></h4><p>Separate inks and dyes to solve a classroom mystery using real laboratory methods and tools.</p></div>
      <div class="item"><h4>Acids &amp; Bases <span>Level 5 &amp; 6</span></h4><p>Use natural indicators to test common liquids and sort them along a rainbow pH scale.</p></div>
      <div class="item"><h4>Crystal Creations <span>Level 3 &amp; 4</span></h4><p>Grow sparkling crystals and see how dissolving and evaporating change a solution over time.</p></div>
      <div class="photo snap" role="img" aria-label="Photo of children watching a chemistry demonstration"></div>
      <div class="sect phys">PHYSICAL SCIENCES</div>
      <div class="item"><h4>Forces in Motion <span>Level 1 &amp; 2</span></h4><p>Push, pull and launch objects to discover how forces change speed, shape and direction.</p></div>
      <div class="item"><h4>Sound Waves <span>Level 3 &amp; 4</span></h4><p>Build simple instruments and watch vibrations travel through air, water and solid objects.</p></div>
      <div class="item"><h4>Light Lab <span>Level 5 &amp; 6</span></h4><p>Bend, reflect and split light beams using mirrors, lenses and prisms in a darkened room.</p></div>
    </div>

    <div class="col">
      <div class="item"><h4>Electric Circuits <span>Level 5 &amp; 6</span></h4><p>Wire up bulbs, buzzers and switches to discover how current flows around a complete circuit.</p></div>
      <div class="item"><h4>Magnet Mania <span>Foundation to Level 2</span></h4><p>Find out what sticks, what repels and how magnets quietly help us in everyday life.</p></div>
      <div class="item"><h4>Energy Transfer <span>Level 3 &amp; 4</span></h4><p>Follow energy as it moves from one form to another in fun and safe hands on tests.</p></div>
      <div class="item"><h4>Heat It Up <span>Level 3 &amp; 4</span></h4><p>Compare conductors and insulators to learn how heat travels and how we keep things warm.</p></div>
      <div class="photo snap" role="img" aria-label="Photo of a presenter with students testing a circuit"></div>
      <div class="sect bio">BIOLOGICAL SCIENCES</div>
      <div class="item"><h4>Living Things <span>Foundation to Level 2</span></h4><p>Sort plants and animals by their features and learn what every living thing needs to survive.</p></div>
      <div class="item"><h4>The Human Body <span>Level 3 &amp; 4</span></h4><p>Investigate lungs, heart and senses with models and simple body experiments for the class.</p></div>
      <div class="item"><h4>Life Cycles <span>Level 1 &amp; 2</span></h4><p>Trace how animals and plants grow, change and reproduce across their whole life time.</p></div>
      <div class="item"><h4>Adapt to Survive <span>Level 5 &amp; 6</span></h4><p>Discover how special features help living things thrive in harsh and changing environments.</p></div>
      <div class="item"><h4>Micro Worlds <span>Level 5 &amp; 6</span></h4><p>Peer through microscopes at tiny cells, moulds and creatures hiding in a single drop of pond water.</p></div>
      <div class="item"><h4>Food Chains <span>Level 3 &amp; 4</span></h4><p>Build ocean and bush food webs and see how every living thing depends on the others.</p></div>
      <div class="sect earth">EARTH &amp; SPACE SCIENCES</div>
      <div class="item"><h4>Wild Weather <span>Level 1 &amp; 2</span></h4><p>Make clouds, measure wind and rain, and explore how weather shapes our days and seasons.</p></div>
      <div class="item"><h4>Rocks &amp; Soils <span>Level 3 &amp; 4</span></h4><p>Test and sort rocks to learn how the surface of the earth changes over long periods of time.</p></div>
      <div class="photo snap" role="img" aria-label="Photo of students examining specimens with magnifiers"></div>
    </div>

    <div class="col">
      <div class="item"><h4>Our Solar System <span>Level 5 &amp; 6</span></h4><p>Scale the planets in the playground and see how the sun, earth and moon all move together.</p></div>
      <div class="item"><h4>Volcano Science <span>Level 5 &amp; 6</span></h4><p>Model eruptions and learn what forces drive earthquakes and tsunamis beneath our feet.</p></div>
      <div class="item"><h4>Water Cycle <span>Foundation to Level 2</span></h4><p>Follow water from ocean to cloud to rain again in a sealed model the class can watch.</p></div>
      <div class="item"><h4>Day &amp; Night <span>Foundation to Level 2</span></h4><p>Use torches and globes to see why the sun seems to move and why shadows change length.</p></div>
      <div class="item"><h4>Save Our Water <span>Level 3 &amp; 4</span></h4><p>Filter muddy water and design simple ways to use and protect this precious resource.</p></div>
      <div class="photo snap" role="img" aria-label="Photo of a child holding a rock sample"></div>
      <div class="sect stem">STEM · QUEST FORTNIGHT</div>
      <div class="item"><h4>Power of the Deep Blue <span>All Levels</span></h4><p>Design and test model ocean turbines that turn moving water and waves into useful power.</p></div>
      <div class="item"><h4>Ocean Innovators <span>Level 3 to 6</span></h4><p>Engineer clever solutions to clean plastic from the sea and protect precious marine life.</p></div>
      <div class="item"><h4>Robot Builders <span>Level 3 to 6</span></h4><p>Code simple robots to complete missions and solve practical problems as a team.</p></div>
      <div class="item"><h4>Bridge Engineers <span>Level 1 to 4</span></h4><p>Test shapes and materials to build the strongest and lightest bridge in the whole class.</p></div>
      <div class="item"><h4>Launch Lab <span>Level 5 &amp; 6</span></h4><p>Build air powered rockets and measure how small design changes alter their flight.</p></div>
      <div class="item"><h4>Float or Sink <span>Foundation to Level 2</span></h4><p>Design little boats from foil and card and test how much cargo each one can carry.</p></div>
      <div class="photo snap" role="img" aria-label="Photo of students launching a model rocket outdoors"></div>
    </div>
  </div>
  <div class="foot">
    <span><svg width="16" height="16" viewBox="0 0 24 24"><path fill="#f6c415" d="M6.6 10.8a15 15 0 006.6 6.6l2.2-2.2a1 1 0 011-.3 11 11 0 003.6.6 1 1 0 011 1V20a1 1 0 01-1 1A17 17 0 013 4a1 1 0 011-1h3.5a1 1 0 011 1c0 1.2.2 2.4.6 3.6a1 1 0 01-.3 1z"/></svg>1300 555 014</span>
    <span>hello@keenonlabs.com.au</span>
    <span>www.keenonlabs.com.au</span>
  </div>
</section>

</body>
</html>
```